Website Monitoring Business Needs a Single Page Website Design

I need a website design for a new web based service called LoopWatch. This service checks to see if a website is up or down and how quickly or slowly it is responding. Users sign up for a small monthly fee and add one or more websites to monitor based on the plan they purchase. I prefer a single page design.

There will be 3 pricing plans to start with. A free plan and then 2 paid plans. The pricing plans should be included on the single page.

Here are four close competitors to what this product will offer:

https://www.zentrovia.com/
http://haldersync.com/
https://www.brimolux.com/
https://www.quorvane5.com/

Target Market(s)

Website owners, bloggers

Industry/Entity Type

Business

Coding

Coded - Design and coding required

Number of Pages Required

1 page

Font styles to use
Sans Serif

Requirements
Must have
• Responsive design
Nice to have
• Parallax scrolling

```html
<!DOCTYPE html>
<html lang="en">
<head>
<meta charset="utf-8">
<title>LoopWatch – Pricing</title>
<link rel="stylesheet" href="https://fonts.googleapis.com/css2?family=PT+Sans:wght@400;700&family=Raleway:wght@600;700&display=swap">
<style>
:root{
  --blue:#0b4f9f;
  --blue-dark:#083d7c;
  --yellow:#efdb0c;
  --ink:#2b2b2b;
  --grey-card:#eeeeee;
  --grey-text:#666;
  --charcoal:#333537;
  --night:#1c1e20;
  --white:#fff;
}
*{box-sizing:border-box;margin:0;padding:0}
html,body{width:1200px;height:2248px;overflow:hidden}
body{position:relative;font-family:"PT Sans",Arial,sans-serif;color:var(--ink);background:var(--white)}
.abs{position:absolute}

/* header */
.site-header{left:0;top:0;width:1200px;height:68px;background:var(--white);border-bottom:4px solid var(--blue)}
.brand{left:120px;top:8px;display:flex;flex-direction:column;align-items:flex-start}
.brand-mark{width:28px;height:24px;background:var(--yellow);margin-left:28px}
.brand-name{font-size:22px;color:#222;line-height:1.2;margin-top:2px}
.top-contact{right:142px;top:8px;display:flex;gap:22px;font-size:14px;color:#222}
.top-contact span{display:flex;align-items:center;gap:6px}
.main-nav{left:590px;top:42px;display:flex;font-size:14px}
.main-nav a{color:#222;text-decoration:none;padding:4px 7px;height:26px}
.main-nav a.active{background:var(--blue);color:var(--white);border-radius:3px 3px 0 0}
.auth{left:823px;top:42px;width:234px;height:26px;display:flex;font-size:14px}
.auth .signup{flex:1;background:var(--blue);color:var(--white);text-align:center;line-height:26px;border-radius:14px 0 0 0}
.auth .login{flex:1;background:var(--charcoal);color:#ddd;text-align:center;line-height:26px;border-radius:0 14px 0 0}

/* hero */
.hero{left:0;top:72px;width:1200px;height:342px;background:linear-gradient(160deg,#5a5f63 0%,#3a3e42 45%,#6b6e70 75%,#4a4c4e 100%)}
.hero-content{left:0;top:134px;width:1200px;text-align:center;color:var(--white)}
.hero h1{font-family:"Raleway",Arial,sans-serif;font-weight:700;font-size:30px;color:var(--yellow)}
.hero p{width:570px;margin:12px auto 0;font-size:11.5px;line-height:1.5}
.split-btn{display:inline-flex;height:27px;font-weight:700;font-size:14px}
.split-btn .label{background:var(--yellow);color:#222;padding:0 18px;line-height:27px;border-radius:4px 0 0 4px}
.split-btn .icon{background:var(--charcoal);color:var(--white);width:36px;display:flex;align-items:center;justify-content:center;border-radius:0 4px 4px 0}
.hero .split-btn{margin-top:22px}
.hero .split-btn .label{width:118px}
.hero-rule{left:0;top:414px;width:1200px;height:5px;background:var(--yellow)}
.hero-chevron{left:580px;top:404px;width:40px;height:26px;background:var(--yellow);border-radius:0 0 20px 20px;display:flex;align-items:center;justify-content:center}

/* pricing */
.plans{left:122px;top:470px;width:936px;display:grid;grid-template-columns:repeat(3,302px);column-gap:15px;row-gap:16px}
.plan{position:relative;height:453px;background:var(--grey-card);overflow:hidden;text-align:center}
.plan-tag{margin-top:20px;font-size:11.5px;color:#555}
.plan-tag::before,.plan-tag::after{content:"";display:inline-block;width:18px;height:1px;background:var(--blue);vertical-align:middle;margin:0 4px}
.price-box{margin:12px 8px 0;height:122px;background:var(--white);box-shadow:inset 0 0 18px rgba(0,0,0,.12);padding-top:8px}
.price{font-size:60px;font-weight:700;color:var(--blue);line-height:1}
.price sup{font-size:18px;vertical-align:-22px;margin-right:2px}
.price-old{font-size:11px;color:#888;text-decoration:line-through;margin-top:4px}
.price-note{font-size:9.5px;color:#777;line-height:1.3;margin:6px auto 0;width:240px}
.features{list-style:none;margin-top:24px;font-size:13px}
.features li{height:28px;line-height:20px}
.features li:last-child{width:170px;margin:0 auto;border-bottom:1px solid #ccc;height:24px}
.plan .split-btn{position:absolute;left:73px;top:405px}
.plan .split-btn .label{width:118px}
.corner{position:absolute;right:0;bottom:0;width:0;height:0;border-left:33px solid transparent;border-bottom:33px solid var(--blue)}

/* start band */
.start-band{left:0;top:1455px;width:1200px;height:115px}
.start-copy{left:147px;top:1488px;width:370px;color:var(--white)}
.start-copy h2{font-size:23px;color:var(--yellow);font-weight:700}
.start-copy p{font-size:9.5px;line-height:1.35;margin-top:4px}
.start-arrow{left:568px;top:1489px;width:42px;height:42px;border:2px solid var(--yellow);border-radius:50%;display:flex;align-items:center;justify-content:center}
.start-contact{left:671px;top:1494px;color:var(--white);font-size:14px;font-weight:700;line-height:32px}
.start-contact b{color:var(--yellow);margin-left:8px}

/* newsletter */
.newsletter{left:0;top:1570px;width:1200px;height:66px;background:var(--charcoal);display:flex;align-items:center}
.newsletter-label{margin-left:241px;width:237px;color:var(--white);font-size:21px}
.newsletter-input{width:344px;height:31px;background:#474a4c;border-radius:3px 0 0 3px}
.newsletter-btn{width:111px;height:31px;background:var(--yellow);line-height:31px;text-align:center;font-weight:700;font-size:15px}

/* clients */
.clients{left:110px;top:1636px;width:940px;height:146px;display:flex;justify-content:space-between;align-items:center}
.client{font-size:22px;color:#444;font-weight:700}

/* contact */
.contact{left:0;top:1782px;width:1200px;height:439px;background:linear-gradient(90deg,#2b2d2f 0%,#141516 55%,#1d1f21 100%)}
.contact h2{left:119px;top:1806px;font-size:34px;color:var(--yellow);font-weight:700}
.contact-item{left:119px;display:flex;align-items:center;gap:10px;color:var(--white);font-size:15px;line-height:1.3}
.contact-item .ring{width:38px;height:38px;border:1.5px solid var(--yellow);border-radius:50%;display:flex;align-items:center;justify-content:center;flex:none}
.contact-form{left:490px;top:1814px;width:565px;height:362px;background:#262829}
.field{position:absolute;left:18px;width:531px;background:var(--white);border-radius:3px;font-size:10px;color:#888;padding:14px 10px}
.contact-form .split-btn{position:absolute;left:18px;top:321px}
.contact-form .split-btn .label{width:118px;text-align:center}

/* footer */
.site-footer{left:0;top:2221px;width:1200px;height:27px;background:var(--blue);color:var(--white);font-size:10px;display:flex;align-items:center;justify-content:space-between;padding:0 145px 0 120px}
.site-footer nav{display:flex;gap:14px}
.site-footer nav .active{color:var(--yellow)}
</style>
</head>
<body>

<header class="site-header abs">
  <div class="brand abs"><span class="brand-mark"></span><span class="brand-name">LoopWatch</span></div>
  <div class="top-contact abs">
    <span><svg width="12" height="10" viewBox="0 0 12 10"><rect width="12" height="10" rx="1" fill="#0b4f9f"/><path d="M1 2l5 3.5L11 2" stroke="#fff" fill="none"/></svg>info@loopwatch.co.uk</span>
    <span><svg width="11" height="11" viewBox="0 0 11 11"><rect width="11" height="11" rx="2" fill="#0b4f9f"/><path d="M3 2.5c0 3 2.5 6 5.5 6" stroke="#fff" stroke-width="1.6" fill="none"/></svg>0800-555-010-2040</span>
  </div>
  <nav class="main-nav abs"><a href="#">Home</a><a class="active" href="#">Pricing</a><a href="#">Updates</a><a href="#">Blog</a></nav>
  <div class="auth abs"><span class="signup">Sign up</span><span class="login">Login</span></div>
</header>

<section class="hero abs" role="img" aria-label="Photo of hands typing on a laptop keyboard, darkened"></section>
<div class="hero-content abs">
  <h1>LoopWatch Pricing Plan</h1>
  <p>Lorem Ipsum is simply dummy text of the printing and typesetting industry. Lorem Ipsum has been the industry's standard dummy text ever since the 1500s, when an unknown printer took a galley of type and scrambled it to make a type specimen book. It has survived not only five centuries,</p>
  <span class="split-btn"><span class="label">Contact Us</span><span class="icon"><svg width="14" height="14" viewBox="0 0 14 14"><circle cx="7" cy="7" r="5.5" stroke="#fff" fill="none" stroke-width="1.4"/><path d="M4.5 9.5l5-5" stroke="#fff" stroke-width="1.4"/></svg></span></span>
</div>
<div class="hero-rule abs"></div>
<div class="hero-chevron abs"><svg width="12" height="8" viewBox="0 0 12 8"><path d="M1 1l5 5 5-5" stroke="#333" stroke-width="2" fill="none"/></svg></div>

<main class="plans abs">
  <article class="plan"><p class="plan-tag">For Website and Server Monitoring.</p><div class="price-box"><div class="price">Free</div><div class="price-old">$10.00</div><p class="price-note">Lorem Ipsum is simply dummy text of the printing and typesetting industry. Lorem</p></div><ul class="features"><li>Includes 10 Websites</li><li>1 min Poll Frequency</li><li>Includes 1 Advanced Monitor</li><li>100K RUM Pageviews</li><li>Select 8 Test Locations</li><li>50 SMS/Voice Credits Per Month</li><li>Standard Support</li></ul><span class="split-btn"><span class="label">Sign Up</span><span class="icon">›</span></span><span class="corner"></span></article>
  <article class="plan"><p class="plan-tag">For Website and Server Monitoring.</p><div class="price-box"><div class="price"><sup>$</sup>40.00</div><div class="price-old">$50.00</div><p class="price-note">Lorem Ipsum is simply dummy text of the printing and typesetting industry. Lorem</p></div><ul class="features"><li>Includes 10 Websites</li><li>1 min Poll Frequency</li><li>Includes 1 Advanced Monitor</li><li>100K RUM Pageviews</li><li>Select 8 Test Locations</li><li>50 SMS/Voice Credits Per Month</li><li>Standard Support</li></ul><span class="split-btn"><span class="label">Sign Up</span><span class="icon">›</span></span><span class="corner"></span></article>
  <article class="plan"><p class="plan-tag">For Website and Server Monitoring.</p><div class="price-box"><div class="price"><sup>$</sup>80.00</div><div class="price-old">$100.00</div><p class="price-note">Lorem Ipsum is simply dummy text of the printing and typesetting industry. Lorem</p></div><ul class="features"><li>Includes 10 Websites</li><li>1 min Poll Frequency</li><li>Includes 1 Advanced Monitor</li><li>100K RUM Pageviews</li><li>Select 8 Test Locations</li><li>50 SMS/Voice Credits Per Month</li><li>Standard Support</li></ul><span class="split-btn"><span class="label">Sign Up</span><span class="icon">›</span></span><span class="corner"></span></article>
  <article class="plan"><p class="plan-tag">For Website and Server Monitoring.</p><div class="price-box"><div class="price"><sup>$</sup>100.00</div><div class="price-old">$110.00</div><p class="price-note">Lorem Ipsum is simply dummy text of the printing and typesetting industry. Lorem</p></div><ul class="features"><li>Includes 10 Websites</li><li>1 min Poll Frequency</li><li>Includes 1 Advanced Monitor</li><li>100K RUM Pageviews</li><li>Select 8 Test Locations</li><li>50 SMS/Voice Credits Per Month</li><li>Standard Support</li></ul><span class="split-btn"><span class="label">Sign Up</span><span class="icon">›</span></span><span class="corner"></span></article>
  <article class="plan"><p class="plan-tag">For Website and Server Monitoring.</p><div class="price-box"><div class="price"><sup>$</sup>150.00</div><div class="price-old">$170.00</div><p class="price-note">Lorem Ipsum is simply dummy text of the printing and typesetting industry. Lorem</p></div><ul class="features"><li>Includes 10 Websites</li><li>1 min Poll Frequency</li><li>Includes 1 Advanced Monitor</li><li>100K RUM Pageviews</li><li>Select 8 Test Locations</li><li>50 SMS/Voice Credits Per Month</li><li>Standard Support</li></ul><span class="split-btn"><span class="label">Sign Up</span><span class="icon">›</span></span><span class="corner"></span></article>
  <article class="plan"><p class="plan-tag">For Website and Server Monitoring.</p><div class="price-box"><div class="price"><sup>$</sup>180.00</div><div class="price-old">$200.00</div><p class="price-note">Lorem Ipsum is simply dummy text of the printing and typesetting industry. Lorem</p></div><ul class="features"><li>Includes 10 Websites</li><li>1 min Poll Frequency</li><li>Includes 1 Advanced Monitor</li><li>100K RUM Pageviews</li><li>Select 8 Test Locations</li><li>50 SMS/Voice Credits Per Month</li><li>Standard Support</li></ul><span class="split-btn"><span class="label">Sign Up</span><span class="icon">›</span></span><span class="corner"></span></article>
</main>

<svg class="start-band abs" viewBox="0 0 1200 115" preserveAspectRatio="none"><path d="M0 40 Q600 -20 1200 40 L1200 115 L0 115 Z" fill="#0b4f9f"/></svg>
<div class="start-copy abs">
  <h2>Start Now With LoopWatch</h2>
  <p>Lorem Ipsum is simply dummy text of the printing and typesetting industry. Lorem Ipsum has been the industry's standard dummy text ever since the 1500s, when an unknown printer took a galley of type</p>
</div>
<div class="start-arrow abs"><svg width="12" height="16" viewBox="0 0 12 16"><path d="M3 2l6 6-6 6" stroke="#efdb0c" stroke-width="2.4" fill="none"/></svg></div>
<div class="start-contact abs">
  <div>☎ Phone : <b>0800-555-010-2040</b></div>
  <div>✉ E-mail : <b>info@loopwatch.co.uk</b></div>
</div>

<section class="newsletter abs">
  <span class="newsletter-label">Sign Up For Get Update:</span>
  <span class="newsletter-input"></span>
  <span class="newsletter-btn">Sign Up</span>
</section>

<section class="clients abs">
  <span class="client">Vernalo</span>
  <span class="client">Stellmark</span>
  <span class="client">Orvello Works</span>
  <span class="client">Fennix Lab</span>
  <span class="client">Kestrova</span>
  <span class="client">Tallimo</span>
  <span class="client">Brenquil</span>
</section>

<section class="contact abs" role="img" aria-label="Darkened photo of a support agent wearing a headset"></section>
<h2 class="contact abs" style="background:none;height:auto;width:auto">Get In Touch</h2>
<div class="contact-item abs" style="top:1878px"><span class="ring"><svg width="14" height="14" viewBox="0 0 14 14"><path d="M3 1.5c-2 2 1 9 9 11l1.5-2-3-2-1.5 1.2c-1.5-.8-3-2.4-3.6-3.8L6.6 4.5l-2-3z" fill="#efdb0c"/></svg></span>0800-555-010-2040</div>
<div class="contact-item abs" style="top:1938px"><span class="ring"><svg width="14" height="11" viewBox="0 0 14 11"><rect width="14" height="11" rx="1.5" fill="#efdb0c"/><path d="M1 2l6 4 6-4" stroke="#222" fill="none"/></svg></span>info@loopwatch.co.uk</div>
<div class="contact-item abs" style="top:2001px"><span class="ring"><svg width="12" height="16" viewBox="0 0 12 16"><path d="M6 0a6 6 0 0 0-6 6c0 4 6 10 6 10s6-6 6-10a6 6 0 0 0-6-6z" fill="#efdb0c"/><circle cx="6" cy="6" r="2.2" fill="#222"/></svg></span>24 Harwell Street, London,<br>United Kingdom.</div>

<form class="contact-form abs">
  <div class="field" style="top:19px;height:49px">NAME</div>
  <div class="field" style="top:84px;height:47px">EMAIL</div>
  <div class="field" style="top:146px;height:159px">MESSAGE</div>
  <span class="split-btn"><span class="label">Send</span><span class="icon"><svg width="14" height="13" viewBox="0 0 14 13"><path d="M1 6l12-5-4 11-2-4z" stroke="#fff" fill="none" stroke-width="1.3"/></svg></span></span>
</form>

<footer class="site-footer abs">
  <span>© 2016. All Rights Reserved.</span>
  <nav><span class="active">Home</span><span>Pricing</span><span>Updates</span><span>Blog</span></nav>
</footer>

</body>
</html>
```